Letterhead for Conveyancing Company

Use existing logo to create a letterhead for a conveyancing company. Must be able to be used in Microsoft Word. Easy to read and professional.
Contact information to be at the bottom.
Bright Wren Conveyancing Pty Ltd
ACN 621 984 736PO Box 535 Campbelltown SA 5074
Mobile - 0461273985
Web address - www.brightwrenconveyancing.com.au

Requirements
Must have
• Logo and contact details.
• Simple and professional.

```html
<!DOCTYPE html>
<html lang="en">
<head>
<meta charset="utf-8">
<title>Bright Wren Conveyancing Letterhead</title>
<link rel="stylesheet" href="https://fonts.googleapis.com/css2?family=Roboto:wght@400;500;700&display=swap">
<style>
  :root {
    --brand-pink: #e0418f;
    --brand-grey: #8a8a8a;
    --text-grey: #8c8c8c;
    --paper: #ffffff;
    --backdrop: #f1f1f1;
  }
  html, body {
    margin: 0;
    padding: 0;
    width: 680px;
    height: 1200px;
    overflow: hidden;
    background: var(--backdrop);
    font-family: "Roboto", sans-serif;
  }
  .canvas {
    position: relative;
    width: 680px;
    height: 1200px;
  }
  .letterhead {
    position: absolute;
    left: 40px;
    top: 212px;
    width: 600px;
    height: 776px;
    background: var(--paper);
    box-shadow: 0 10px 30px rgba(0, 0, 0, 0.18);
  }
  .brand-name {
    position: absolute;
    right: 50px;
    top: 36px;
    margin: 0;
    text-align: right;
    color: var(--brand-pink);
    font-weight: 700;
    font-size: 28px;
    line-height: 30px;
    letter-spacing: -0.5px;
  }
  .footer-band {
    position: absolute;
    left: 0;
    top: 692px;
    width: 600px;
    height: 11px;
  }
  .contact {
    position: absolute;
    top: 720px;
    font-size: 11.5px;
    line-height: 15px;
    color: var(--text-grey);
  }
  .contact p {
    margin: 0;
    display: flex;
    align-items: center;
    gap: 4px;
  }
  .contact-company { left: 48px; }
  .contact-company .company-name {
    font-weight: 700;
    text-transform: uppercase;
    display: block;
  }
  .contact-reach { left: 355px; }
  .icon { width: 10px; height: 10px; flex: none; }
</style>
</head>
<body>
<div class="canvas">
  <section class="letterhead">
    <h1 class="brand-name">Bright Wren<br>Conveyancing</h1>

    <svg class="footer-band" viewBox="0 0 600 11" aria-hidden="true">
      <polygon points="0,0 327,0 338,11 0,11" fill="var(--brand-pink)"/>
      <polygon points="334,0 600,0 600,11 345,11" fill="var(--brand-grey)"/>
    </svg>

    <div class="contact contact-company">
      <span class="company-name">Bright Wren Conveyancing Pty Ltd</span>
      <p>
        <svg class="icon" viewBox="0 0 10 10" aria-hidden="true"><path d="M5 0a3.4 3.4 0 0 1 3.4 3.4C8.4 6 5 10 5 10S1.6 6 1.6 3.4A3.4 3.4 0 0 1 5 0z" fill="var(--brand-pink)"/><circle cx="5" cy="3.4" r="1.2" fill="#fff"/></svg>
        ACN 738 215 490PO Box 862 Marlow Heights SA 5093
      </p>
    </div>

    <div class="contact contact-reach">
      <p>
        <svg class="icon" viewBox="0 0 10 10" aria-hidden="true"><path d="M0 3c0-1.5 2-2.5 5-2.5S10 1.5 10 3v1H7.5V3h-5v1H0zM2 4.5h6L9 9H1z" fill="var(--brand-pink)"/><circle cx="5" cy="6.6" r="1.1" fill="#fff"/></svg>
        0461273985
      </p>
      <p>
        <svg class="icon" viewBox="0 0 10 10" aria-hidden="true"><g fill="none" stroke="var(--brand-pink)" stroke-width="0.9"><circle cx="5" cy="5" r="4.4"/><ellipse cx="5" cy="5" rx="2" ry="4.4"/><line x1="0.6" y1="5" x2="9.4" y2="5"/></g></svg>
        www.brightwrenconveyancing.com.au
      </p>
    </div>
  </section>
</div>
</body>
</html>
```